hawkforge structural steel

8 1/2" x 11" flyer color both sides. Use at least 12 pictures.

Add the word; structural under HawkForge to logo

bullet points:
Laser Accuracy
On-time scheduling
Own our Equipment
39 Years Exp.
Manufacturing Construction Brackets Since 1982
We manufacture custom ibeams in Phoenix, AZ
Certified welders

Hawkforge Plant
2814 n. 17th avenue, suite-3
Phx, AZ 85019
480-629-8107

Target Market(s)

Architects, builders

Industry/Entity Type

construction

Colors
0054AA
0677BA
7BADD7
CADEEF
E8F1F8

```html
<!DOCTYPE html>
<html lang="en">
<head>
<meta charset="utf-8">
<title>HawkForge Structural Flyer</title>
<link rel="stylesheet" href="https://fonts.googleapis.com/css2?family=Archivo:wght@400;500;600;700&display=swap">
<style>
  :root {
    --navy: #1c1f45;
    --white: #ffffff;
    --backdrop: #e6e6e6;
    --ink: #1c1f45;
  }
  * { margin: 0; padding: 0; box-sizing: border-box; }
  html, body { width: 1200px; height: 1000px; overflow: hidden; }
  body { background: var(--backdrop); font-family: "Archivo", sans-serif; color: var(--ink); position: relative; }
  .flyer { position: absolute; left: 300px; top: 83px; width: 572px; height: 812px; background: var(--white); overflow: hidden; }
  .header-art { position: absolute; left: 0; top: 0; width: 572px; height: 237px; }
  .brand { position: absolute; left: 345px; top: 78px; width: 230px; text-align: center; color: var(--white); font-weight: 500; font-size: 25px; line-height: 28px; letter-spacing: 0.5px; }
  .brand-mark { display: block; width: 14px; height: 14px; border-radius: 50%; background: var(--white); margin: 0 auto 26px; }
  .tagline { position: absolute; left: 0; top: 264px; width: 572px; text-align: center; font-weight: 700; font-size: 19.5px; line-height: 25px; letter-spacing: 0.3px; }
  .services-title { position: absolute; left: 147px; top: 328px; font-weight: 700; font-size: 32px; line-height: 40px; }
  .services { position: absolute; left: 148px; top: 373px; list-style: none; font-size: 25px; line-height: 35px; font-weight: 500; }
  .services li { position: relative; }
  .services li:nth-child(1) { margin-bottom: 10px; }
  .services li:nth-child(2) { margin-bottom: 6px; }
  .services li::before { content: ""; position: absolute; left: -24px; top: 13px; width: 10px; height: 10px; border-radius: 50%; background: var(--navy); }
  .contact { position: absolute; left: 114px; display: flex; align-items: flex-start; font-size: 19px; line-height: 27px; font-weight: 500; }
  .contact svg { width: 28px; height: 28px; margin-right: 20px; flex: none; }
  .contact-address { top: 603px; }
  .contact-phone { top: 718px; align-items: center; }
  .footer-band { position: absolute; left: 0; bottom: 0; width: 572px; height: 38px; background: var(--navy); }
</style>
</head>
<body>
  <main class="flyer">
    <svg class="header-art" viewBox="0 0 572 237">
      <defs>
        <linearGradient id="weldGlow" x1="0" y1="0" x2="1" y2="1">
          <stop offset="0" stop-color="#c9c9d2"/>
          <stop offset="0.45" stop-color="#6d6a80"/>
          <stop offset="1" stop-color="#3a2c2c"/>
        </linearGradient>
      </defs>
      <polygon role="img" aria-label="Photo of a welder in gloves welding steel with bright sparks" points="0,0 365,0 260,117 350,237 0,237" fill="url(#weldGlow)"/>
      <polygon points="392,0 572,0 572,237 390,237 297,117" fill="var(--navy)"/>
    </svg>
    <div class="brand"><span class="brand-mark"></span>HAWKFORGE<br>STRUCTURAL</div>

    <p class="tagline">MANUFACTURING CONSTRUCTION BRACKETS<br>SINCE 1982.</p>

    <h2 class="services-title">OUR SERVICES:</h2>
    <ul class="services">
      <li>LASER ACCURACY</li>
      <li>ON-TIME SCHEDULING</li>
      <li>MANUFACTURING A CUSTOM<br>IBEAMS IN PHOENIX, AZ</li>
      <li>OWN OUR EQUIPMENT</li>
    </ul>

    <div class="contact contact-address">
      <svg viewBox="0 0 28 28" aria-hidden="true">
        <circle cx="14" cy="14" r="14" fill="var(--navy)"/>
        <path d="M14 5a6 6 0 0 0-6 6c0 4.6 6 10 6 10s6-5.4 6-10a6 6 0 0 0-6-6z" fill="none" stroke="#fff" stroke-width="1.8"/>
        <circle cx="14" cy="11" r="2.2" fill="#fff"/>
        <path d="M8 22.5h12" stroke="#fff" stroke-width="1.6"/>
      </svg>
      <p>HAWKFORGE PLANT<br>2814 N. 17TH AVENUE, SUITE-3<br>PHX, AZ 85019</p>
    </div>

    <div class="contact contact-phone">
      <svg viewBox="0 0 28 28" aria-hidden="true">
        <circle cx="14" cy="14" r="14" fill="var(--navy)"/>
        <path d="M9.5 7l2.8 3.2-1.6 2c1 2.2 2.6 3.8 4.8 4.8l2-1.6 3.2 2.8-1.3 2.4c-6-.4-10.9-5.3-11.3-11.3z" fill="#fff"/>
      </svg>
      <p>480-629-8107</p>
    </div>

    <div class="footer-band"></div>
  </main>
</body>
</html>
```